Information Technology Company needs a Website...

We need a single page website for new technology company called:

MERIVALE CREST TECHNOLOGY GROUP
Based in Ojai CA.

We are offering three primary services:

- Business Solutions

- IT Services

- Software Implementation and Consulting

We want a single page design where all content scrolls down/up on one page. We're looking for the following characteristics:

- Home/Landing
- Active background with panoramic view (Will provide content)

- Business Solutions, IT Services, Software Implementation and Consulting

List of software vendors we recommend (Company logos)

- About
- History
- Our Team
- Partners

I'll upload our new logo as soon as we get the design files. I'll also send over some example website layout's that we like shortly.

Target Market(s)

Small/Medium Businesses

Industry/Entity Type

Information Technology

Number of Pages Required

1 page

Font styles to use
Other font styles liked:
• Sansation

Requirements
Must have
• Full page browser width, easy navigation and visibility. Creative design, not like every other "Technology" website template. Should be the "One Page" design where each section is below the next and the user scrolls down the page through the whole site. I like the concept of the following website in the main "Whiteboard" image:
• http://www.plinkoria-sample.com/design/4082913
• And the way this site does the active panoramic background:
• http://www.vantrelwork-sample.com/
• Something interesting and appealing to potential clients looking for Small/Medium business solutions and IT Services.
• Use uploaded Logo to establish color and theme for website.
Should not have
• Look the same as every other information technology website template.

```html
<!DOCTYPE html>
<html lang="en">
<head>
<meta charset="utf-8">
<title>Merivale Crest Technology Group</title>
<link rel="stylesheet" href="https://fonts.googleapis.com/css2?family=Open+Sans:wght@400;600;700&display=swap">
<style>
:root{
  --orange:#f26a21;
  --orange-light:#f7941d;
  --orange-deep:#e2561a;
  --ink:#333a44;
  --muted:#7a808a;
  --panel:#ffffff;
  --page:#eef0f3;
  --line:#dfe2e7;
  --vendor:#5a6472;
}
*{box-sizing:border-box;margin:0;padding:0}
html,body{width:1200px;height:2620px;overflow:hidden}
body{position:relative;background:var(--page);font-family:"Open Sans",Arial,sans-serif;color:var(--ink)}
.abs{position:absolute}

/* header */
.site-header{left:0;top:0;width:1200px;height:62px;background:#fff;z-index:3}
.brand{left:28px;top:16px;display:flex;align-items:center;gap:8px;font-weight:700;font-size:18px;color:var(--orange);letter-spacing:.5px}
.brand-dot{width:14px;height:14px;border-radius:50%;background:var(--orange)}
.menu-toggle{right:36px;top:20px;width:26px}
.menu-toggle span{display:block;height:3px;background:#555;margin-bottom:5px}

/* hero */
.hero{left:0;top:62px;width:1200px;height:560px;overflow:hidden}
.hero-photo{left:0;top:0;width:1200px;height:560px;background:linear-gradient(120deg,#c9ccd1 0%,#e6e3df 45%,#9aa1ab 100%)}
.hero-shape{left:0;top:0}
.hero-title{left:90px;top:205px;color:#fff;text-transform:uppercase}
.hero-title .lead{font-size:26px;font-weight:400;letter-spacing:1px}
.hero-title .main{font-size:46px;font-weight:700;line-height:1.1}
.hero-btn{left:92px;top:322px;padding:8px 22px;border:2px solid #fff;color:#fff;font-size:13px;font-weight:600;border-radius:2px}
.hero-arrow{top:324px;width:32px;height:32px;border-radius:50%;background:rgba(60,60,60,.55)}
.hero-arrow svg{display:block;margin:9px auto}

/* panels */
.panel{background:var(--panel);box-shadow:0 1px 3px rgba(0,0,0,.08)}
.section-title{width:1200px;left:0;text-align:center;font-size:30px;font-weight:400;color:var(--ink)}
.section-title::after{content:"";display:block;width:44px;height:3px;background:var(--orange);margin:10px auto 0}

.services{left:88px;top:585px;width:1024px;height:300px}
.service{top:110px;width:290px}
.service-head{display:flex;gap:12px;align-items:flex-start}
.service-icon{width:34px;height:30px;flex:none}
.service-name{font-size:17px;font-weight:600;color:var(--ink);line-height:1.25}
.service-text{margin-top:14px;font-size:13px;line-height:1.6;color:var(--muted)}

.story{height:222px}
.story-image{width:220px;height:170px;background:linear-gradient(135deg,#8e98a6,#d7dbe1)}
.story-title{font-size:30px;font-weight:400}
.story-title::after{content:"";display:block;width:44px;height:3px;background:var(--orange);margin-top:8px}
.story-title.right::after{margin-left:auto}
.story-text{font-size:13.5px;line-height:1.7;color:var(--muted)}

.vendors{left:0;top:1520px;width:1200px;height:200px;background:#fff}
.vendor-row{left:130px;top:100px;width:940px;display:flex;justify-content:space-between;align-items:center}
.vendor{font-size:34px;font-weight:600;color:var(--vendor)}

.team-card{top:1805px;width:220px;text-align:center}
.team-photo{width:220px;height:236px;background:linear-gradient(160deg,#b7bdc6,#e9ebee)}
.team-photo.accent{background:linear-gradient(160deg,var(--orange-light),var(--orange))}
.team-name{margin-top:12px;font-size:16px;font-weight:600}
.team-role{font-size:12.5px;color:var(--muted)}

.partners{left:160px;top:2220px;width:880px;display:flex;justify-content:space-between}
.partner-badge{width:90px;height:90px;border-radius:50%;background:#c9cdd3}
.partner-badge.square{border-radius:10px}

/* footer */
.site-footer{left:0;top:2370px;width:1200px;height:200px;background:linear-gradient(100deg,var(--orange-deep),var(--orange) 50%,var(--orange-light))}
.foot-col{top:30px;width:230px;color:#fff;font-size:13px;line-height:1.7}
.foot-col h4{font-size:14px;font-weight:700;letter-spacing:.5px;margin-bottom:10px;text-transform:uppercase}
.foot-col ul{list-style:none}
.foot-input{margin-top:10px;width:210px;height:30px;background:#fff;color:#999;font-size:12px;padding:6px 10px}
.bottom-bar{left:0;top:2570px;width:1200px;height:50px;background:var(--orange-deep);color:#fff;font-size:12px}
.copyright{left:40px;top:17px}
.social{top:14px;width:22px;height:22px;background:rgba(255,255,255,.85)}
</style>
</head>
<body>

<header class="site-header abs">
  <div class="brand abs"><span class="brand-dot"></span>MERIVALE CREST</div>
  <div class="menu-toggle abs"><span></span><span></span><span></span></div>
</header>

<section class="hero abs">
  <div class="hero-photo abs" role="img" aria-label="Team of business professionals in a bright office"></div>
  <svg class="hero-shape abs" width="1200" height="560" viewBox="0 0 1200 560">
    <defs>
      <linearGradient id="heroOrange" x1="0" y1="0" x2="1" y2="1">
        <stop offset="0" stop-color="#f7941d" stop-opacity=".92"/>
        <stop offset="1" stop-color="#f26a21" stop-opacity=".95"/>
      </linearGradient>
    </defs>
    <polygon points="0,0 320,0 560,560 0,560" fill="url(#heroOrange)"/>
    <polygon points="860,0 1000,0 1200,330 1200,470" fill="#f26a21" opacity=".85"/>
    <polygon points="0,480 1200,430 1200,560 0,560" fill="#ffffff"/>
  </svg>
  <div class="hero-title abs">
    <div class="lead">Welcome to Merivale Crest</div>
    <div class="main">Technology Group</div>
  </div>
  <div class="hero-btn abs">Learn more</div>
  <div class="hero-arrow abs" style="left:24px"><svg width="12" height="14"><path d="M9 1 3 7l6 6" stroke="#fff" stroke-width="2" fill="none"/></svg></div>
  <div class="hero-arrow abs" style="right:24px"><svg width="12" height="14"><path d="m3 1 6 6-6 6" stroke="#fff" stroke-width="2" fill="none"/></svg></div>
</section>

<section class="services panel abs">
  <h2 class="section-title abs" style="left:-88px;top:28px;">Our Primary Services</h2>
  <div class="service abs" style="left:40px">
    <div class="service-head">
      <svg class="service-icon" viewBox="0 0 34 30"><rect x="2" y="8" width="30" height="20" rx="2" fill="none" stroke="#f26a21" stroke-width="2"/><rect x="12" y="3" width="10" height="5" fill="none" stroke="#f26a21" stroke-width="2"/></svg>
      <div class="service-name">Business Solutions</div>
    </div>
    <p class="service-text">Tailored systems that help small teams work faster, plan better and keep daily operations running smoothly.</p>
  </div>
  <div class="service abs" style="left:362px">
    <div class="service-head">
      <svg class="service-icon" viewBox="0 0 34 30"><rect x="2" y="3" width="30" height="18" rx="2" fill="none" stroke="#3b7dd8" stroke-width="2"/><path d="M12 27h10M17 21v6" stroke="#3b7dd8" stroke-width="2"/></svg>
      <div class="service-name">IT Services</div>
    </div>
    <p class="service-text">Reliable support, network care and hardware setup so your office stays online and your people stay productive.</p>
  </div>
  <div class="service abs" style="left:684px">
    <div class="service-head">
      <svg class="service-icon" viewBox="0 0 34 30"><rect x="2" y="3" width="30" height="24" rx="2" fill="none" stroke="#d93b3b" stroke-width="2"/><path d="M2 10h30" stroke="#d93b3b" stroke-width="2"/></svg>
      <div class="service-name">Software Implementation &amp; Consulting</div>
    </div>
    <p class="service-text">We select, install and tune the right software, then guide your staff until every tool feels familiar.</p>
  </div>
</section>

<section class="story panel abs" style="left:88px;top:978px;width:1024px;">
  <div class="story-image abs" style="left:18px;top:-12px" role="img" aria-label="Laptop and office desk scene"></div>
  <h2 class="story-title abs" style="left:270px;top:22px">About us</h2>
  <p class="story-text abs" style="left:270px;top:86px;width:720px">Merivale Crest pairs local attention with deep technical skill. We listen first, map how your business really works, and then build a technology plan that fits your budget and your goals. From the first call to long-term care, one friendly team stays with you and explains every step in plain language.</p>
</section>

<section class="story panel abs" style="left:88px;top:1265px;width:1024px;">
  <div class="story-image abs" style="right:18px;top:-12px;background:linear-gradient(135deg,#d9c7b0,#f1e9df)" role="img" aria-label="Charts and documents on a desk"></div>
  <h2 class="story-title right abs" style="right:270px;top:22px;text-align:right">Our History</h2>
  <p class="story-text abs" style="left:40px;top:86px;width:700px;text-align:right">Founded in Ojai, California, our group began as a small help desk for neighbouring shops and offices. Word spread, projects grew, and today we support businesses across the region with consulting, managed services and software rollouts, while keeping the same personal care that started it all.</p>
</section>

<section class="vendors abs">
  <h2 class="section-title abs" style="top:22px">Software Vendors We Recommend</h2>
  <div class="vendor-row abs">
    <div class="vendor">Norvale</div>
    <div class="vendor">Quadrix</div>
    <div class="vendor">Bexor</div>
    <div class="vendor">Calyptra</div>
  </div>
</section>

<h2 class="section-title abs" style="top:1740px">Our Team</h2>
<div class="team-card abs" style="left:130px"><div class="team-photo" role="img" aria-label="Portrait of team member"></div><div class="team-name">Alden Voss</div><div class="team-role">Position in company</div></div>
<div class="team-card abs" style="left:370px"><div class="team-photo" role="img" aria-label="Portrait of team member"></div><div class="team-name">Mira Castell</div><div class="team-role">Position in company</div></div>
<div class="team-card abs" style="left:610px"><div class="team-photo accent" role="img" aria-label="Portrait of team member"></div><div class="team-name">Tobin Hale</div><div class="team-role">Position in company</div></div>
<div class="team-card abs" style="left:850px"><div class="team-photo" role="img" aria-label="Portrait of team member"></div><div class="team-name">Renata Quill</div><div class="team-role">Position in company</div></div>

<h2 class="section-title abs" style="top:2128px">Our Partners</h2>
<div class="partners abs">
  <div class="partner-badge"></div>
  <div class="partner-badge square"></div>
  <div class="partner-badge"></div>
  <div class="partner-badge"></div>
  <div class="partner-badge square"></div>
</div>

<footer class="site-footer abs">
  <div class="foot-col abs" style="left:40px">
    <h4>About us</h4>
    <p>Technology partner for small and medium businesses, offering practical solutions, dependable support and honest advice.</p>
  </div>
  <div class="foot-col abs" style="left:330px;width:160px">
    <h4>Useful links</h4>
    <ul><li>Our Services</li><li>Our Team</li><li>Contact Us</li><li>About Us</li></ul>
  </div>
  <div class="foot-col abs" style="left:540px;width:260px">
    <h4>Newsletter</h4>
    <p>Sign up for short monthly notes on tools, security tips and company news.</p>
    <div class="foot-input">Email address</div>
  </div>
  <div class="foot-col abs" style="left:880px;width:290px">
    <h4>Contact</h4>
    <p>2480 Laurel Row, Suite 4, Ojai CA 93023</p>
    <p>+1 805 555 0147</p>
    <p>hello@merivalecrest-sample.com</p>
  </div>
</footer>
<div class="bottom-bar abs">
  <div class="copyright abs">© Merivale Crest Technology Group. All rights reserved.</div>
  <div class="social abs" style="right:70px"></div>
  <div class="social abs" style="right:40px"></div>
</div>

</body>
</html>
```